Pharmacy handmade, Personalized Medical Cosmetics Label

Medical Cosmetics label, elegant and professional looking. The creams are Dermatologist formulated and are prepared by local Pharmacy. The label should be versatile and allow space for hand writing to be filled by the pharmacist preparing the product.
The following information will be handwritten:
Upper lid - Lid Balm No.5 ; Marigold, Retinol ; 30
Lower Bottom - Teodora Halvik ; Signature ; 01.01.2017
Upper Lid Label
Velluto Skin (logo)
Doctor Series
(circular pattern - Doctor Formulated, Registered Pharmacy, Handmade, Highest Medical Standards)
(Lid Balm No.5 - in hand writing and different color, maybe red)
Key Ingredients: (Marigold, Retinol - in hand writing, same color as above, maybe red)
(box with hand writing 30) ml
Lower Bottom Label (underneath surface of the container)
Made for Velluto Skin by
Pharmacy Lorant, 7 Pelister blvd., Sofia, ph. 0893517460
Patient: (Teodora Halvik- in hand writing)
Pharmacist: (Signature - in hand writing)
Date: (01.01.2017 - in hand writing)
For External Use
good for 60 days after preparation
Ingredients: Retinol, Marigold Extract, Water, Glycerin, Stearyl Alcohol, Wheat Germ Oil, Polysorbate 60, Sesame Oil, Myristyl Myristate, Cetyl Alcohol, Sorbitan Stearate, Phenoxyethanol, Calendula Extract, Cornflower Extract, Sodium Alginate, Sodium Citrate.
The container lid and bottom are 5 cm = 50 mm in diameter. Made from aluminum and contain 30ml or 50ml.
Please refer to the screen shots from my Web Site to get the feeling for the color pallet and professional look. These creams will be sold on this website. They are custom made by a registered Pharmacy right on the spot after the order has been placed. This is why I need more space for the hand written notes made by the pharmacist who prepared the order.
Please make the design professional, simple and serious colors, like light brown, beige, black or dark brown letters, red hand writing (will be filled by pen or thin marker by the Pharmacist by hand, depending on the order, patient name, etc.)
Thank you.
female 24 - 49 year old
Medical

```html
<!DOCTYPE html>
<html lang="en">
<head>
<meta charset="utf-8">
<title>Velluto Skin – Doctor Series Label Options</title>
<link href="https://fonts.googleapis.com/css2?family=Dancing+Script:wght@500&family=Lora:ital@1&family=Open+Sans:wght@400;700&display=swap" rel="stylesheet">
<style>
  :root {
    --ink: #2f2b29;
    --ink-soft: #4a4542;
    --hand-red: #c61f27;
    --beige-deep: #cfc7c0;
    --beige-mid: #e2dcd6;
    --beige-light: #f3f0ed;
    --band: #d9d2cb;
    --paper: #ffffff;
  }
  html, body { margin: 0; padding: 0; overflow: hidden; background: var(--paper); }
  .canvas { display: block; width: 1181px; height: 1200px; }
  .option-number { font-family: "Open Sans", Arial, sans-serif; font-size: 32px; fill: var(--ink); text-anchor: middle; }
  .ring-text { font-family: "Open Sans", Arial, sans-serif; font-size: 15px; fill: var(--ink-soft); letter-spacing: 1.5px; }
  .brand-name { font-family: "Open Sans", Arial, sans-serif; font-size: 25px; font-weight: 400; fill: var(--ink); text-anchor: middle; }
  .series-name { font-family: "Lora", Georgia, serif; font-style: italic; font-size: 20px; fill: var(--ink-soft); text-anchor: middle; }
  .handwriting { font-family: "Dancing Script", cursive; fill: var(--hand-red); }
  .product-name { font-size: 46px; text-anchor: middle; }
  .key-ingredients { font-size: 34px; text-anchor: middle; }
  .volume-hand { font-size: 26px; text-anchor: end; }
  .caption { font-family: "Open Sans", Arial, sans-serif; fill: var(--ink); }
  .caption-center { text-anchor: middle; }
  .field-label { text-anchor: end; font-size: 13px; }
  .field-value { font-size: 27px; }
  .ingredients-title { font-weight: 700; font-size: 12px; text-anchor: middle; }
  .ingredients-list { font-size: 9px; text-anchor: middle; }
</style>
</head>
<body>
<svg class="canvas" viewBox="0 0 1181 1200" xmlns="http://www.w3.org/2000/svg" xmlns:xlink="http://www.w3.org/1999/xlink">
  <defs>
    <radialGradient id="label-backdrop" cx="50%" cy="50%" r="50%">
      <stop offset="0%" stop-color="var(--beige-light)"/>
      <stop offset="70%" stop-color="var(--beige-mid)"/>
      <stop offset="100%" stop-color="var(--beige-deep)"/>
    </radialGradient>
    <clipPath id="base-face">
      <circle r="158"/>
    </clipPath>
    <path id="ring-path" d="M -150,20 A 151,151 0 1,1 -150,21 Z"/>
    <path id="ring-path-wide" d="M -164,20 A 165,165 0 1,1 -164,21 Z"/>

    <!-- shared logo: name with a plain circle -->
    <g id="brand-lockup">
      <circle cx="-88" cy="-8" r="9" fill="none" stroke="var(--ink)" stroke-width="1.5"/>
      <text class="brand-name" x="12" y="0">Velluto Skin</text>
    </g>

    <!-- lid label core content -->
    <g id="lid-content">
      <use xlink:href="#brand-lockup" transform="translate(0,-74)"/>
      <rect x="-135" y="-62" width="270" height="26" fill="var(--band)"/>
      <line x1="-135" y1="-34" x2="135" y2="-34" stroke="var(--paper)" stroke-dasharray="1 2"/>
      <text class="series-name" x="0" y="-42">Doctor Series</text>
      <text class="handwriting product-name" x="0" y="14">Lid Balm No.5</text>
      <text class="caption caption-center" x="0" y="46" font-size="14">KEY INGREDIENTS:</text>
      <text class="handwriting key-ingredients" x="0" y="88">Marigold, Retinol</text>
      <text class="handwriting volume-hand" x="-2" y="122">30</text>
      <text class="caption" x="4" y="122" font-size="15">ml</text>
    </g>

    <!-- lid label, ring text inside the backdrop -->
    <g id="lid-label">
      <circle r="170" fill="url(#label-backdrop)"/>
      <circle r="136" fill="var(--paper)" fill-opacity="0.78"/>
      <circle r="136" fill="none" stroke="var(--ink-soft)" stroke-width="0.8" stroke-dasharray="1.5 2.5"/>
      <text class="ring-text"><textPath xlink:href="#ring-path" textLength="935" lengthAdjust="spacing">Doctor Formulated • Registered Pharmacy • Handmade • Highest Medical Standards •</textPath></text>
      <use xlink:href="#lid-content"/>
    </g>

    <!-- base label -->
    <g id="base-label">
      <circle r="172" fill="url(#label-backdrop)"/>
      <circle r="158" fill="var(--paper)" fill-opacity="0.8"/>
      <g clip-path="url(#base-face)">
        <rect x="-160" y="-86" width="320" height="32" fill="var(--band)" fill-opacity="0.6"/>
        <line x1="-160" y1="-86" x2="160" y2="-86" stroke="var(--ink-soft)" stroke-width="0.6" stroke-dasharray="1 2"/>
        <line x1="-160" y1="-54" x2="160" y2="-54" stroke="var(--ink-soft)" stroke-width="0.6" stroke-dasharray="1 2"/>
      </g>
      <circle r="158" fill="none" stroke="var(--ink-soft)" stroke-width="0.8" stroke-dasharray="1.5 2.5"/>
      <text class="caption caption-center" x="0" y="-131" font-size="13">MADE FOR</text>
      <use xlink:href="#brand-lockup" transform="translate(0,-97)"/>
      <text class="caption caption-center" x="0" y="-72" font-size="12">Pharmacy Lorant, 7 Pelister blvd., Sofia,</text>
      <text class="caption caption-center" x="0" y="-59" font-size="12">ph. 0893517460</text>
      <text class="caption field-label" x="-90" y="-30">Patient:</text>
      <text class="handwriting field-value" x="-82" y="-28">Teodora Halvik</text>
      <text class="caption field-label" x="-47" y="-2">Pharmacist:</text>
      <text class="handwriting field-value" x="-40" y="0">Signature</text>
      <text class="caption field-label" x="-47" y="25">Date:</text>
      <text class="handwriting field-value" x="-40" y="27" font-size="24">01.01.2017</text>
      <text class="caption caption-center" x="0" y="45" font-size="10.5">For External Use. Good for 60 days after preparation</text>
      <text class="caption ingredients-title" x="0" y="61">Ingredients:</text>
      <text class="caption ingredients-list" x="0" y="75">Retinol, Marigold Extract, Water, Glycerin, Stearyl Alcohol,</text>
      <text class="caption ingredients-list" x="0" y="87">Wheat Germ Oil, Polysorbate 60, Sesame Oil, Myristyl</text>
      <text class="caption ingredients-list" x="0" y="99">Myristate, Cetyl Alcohol, Sorbitan Stearate,</text>
      <text class="caption ingredients-list" x="0" y="111">Phenoxyethanol, Calendula Extract, Cornflower</text>
      <text class="caption ingredients-list" x="0" y="123">Extract, Sodium Alginate,</text>
      <text class="caption ingredients-list" x="0" y="135">Sodium Citrate.</text>
    </g>
  </defs>

  <!-- option numbers -->
  <text class="option-number" x="211" y="118">1</text>
  <text class="option-number" x="590" y="118">2</text>
  <text class="option-number" x="969" y="118">3</text>

  <!-- option 1 -->
  <use xlink:href="#lid-label" transform="translate(211,307)"/>
  <use xlink:href="#base-label" transform="translate(211,675)"/>

  <!-- option 2: ring text on an outer line frame -->
  <g class="lid-label-framed" transform="translate(590,307)">
    <circle r="178" fill="var(--paper)" stroke="var(--ink-soft)" stroke-width="0.8"/>
    <circle r="150" fill="url(#label-backdrop)" stroke="var(--ink-soft)" stroke-width="0.8"/>
    <circle r="128" fill="var(--paper)" fill-opacity="0.6"/>
    <text class="ring-text"><textPath xlink:href="#ring-path-wide" textLength="1020" lengthAdjust="spacing">Doctor Formulated • Registered Pharmacy • Handmade • Highest Medical Standards •</textPath></text>
    <use xlink:href="#lid-content"/>
  </g>
  <use xlink:href="#base-label" transform="translate(590,680)"/>

  <!-- option 3 -->
  <use xlink:href="#lid-label" transform="translate(969,304)"/>
  <use xlink:href="#base-label" transform="translate(969,677)"/>
</svg>
</body>
</html>
```